flyer for roofing advertising

Need a modern, bold, luxurious advertisement flyer for our roofing company. located in buffalo, ny. Big house with a intense roof design asphalt shingles. slogan is "Reliability starts at the top". Colors varies but want it to be modern. we will be handing these out when we are working in the area. phone number is 716-555-0147 for the NO K.W estimate. also our services are roofing, roof repairs, gutters, attic ventilation. we offer a 15 year warranty with our platinum roof program. We are certified by dwellmatch, harlan trevisk, quarno. Also follow us on linkpage, wexora and frunt. website is ktw-roofing.com, linkpage is ktwroofing. pictures are on linkpage and our website if need more can be provided. also can include a review we have.

```html
<!DOCTYPE html>
<html lang="en">
<head>
<meta charset="utf-8">
<title>NO K.W Roofing Flyer</title>
<link href="https://fonts.googleapis.com/css2?family=Montserrat:wght@500;600;700;800;900&display=swap" rel="stylesheet">
<style>
  :root {
    --orange: #d66a14;
    --orange-light: #ef8a2a;
    --charcoal: #2b2d30;
    --ink: #1e1f22;
    --grey: #6e6f72;
    --grey-light: #9a9b9e;
    --page: #e9e9ea;
    --paper: #ffffff;
  }
  * { box-sizing: border-box; margin: 0; padding: 0; }
  html, body { width: 1200px; height: 1200px; overflow: hidden; }
  body { background: var(--page); font-family: "Montserrat", sans-serif; color: var(--ink); }
  .flyer { position: absolute; left: 175px; top: 0; width: 850px; height: 1200px; background: var(--paper); overflow: hidden; }
  .hero-photo { position: absolute; left: 0; top: 0; width: 850px; height: 640px;
    background: linear-gradient(160deg, #f3e9e4 0%, #d9c7bd 25%, #8f7e72 55%, #5d5048 80%, #cfd3d6 100%); }
  .logo-slab { position: absolute; left: 0; top: 470px; width: 300px; height: 170px; background: var(--charcoal);
    clip-path: polygon(0 0, 100% 0, 82% 100%, 0 100%); display: flex; align-items: center; padding-left: 34px; gap: 12px; }
  .logo-slab .mark { width: 18px; height: 18px; background: var(--orange); }
  .logo-slab .name { font-weight: 800; font-size: 38px; color: var(--orange); letter-spacing: 1px; }
  .gallery { position: absolute; left: 570px; top: 470px; width: 260px; }
  .gallery .photo { height: 170px; margin-bottom: 12px; border: 5px solid var(--orange); }
  .photo.roof { background: linear-gradient(180deg, #6c9ad4 0%, #8a8173 55%, #4f4a45 100%); }
  .photo.siding { background: linear-gradient(135deg, #4a4e57 0%, #7b818a 50%, #2f3f7a 100%); }
  .photo.gutter { background: linear-gradient(135deg, #9fc0e0 0%, #d8d1ba 45%, #b8ae8e 100%); }
  .headline { position: absolute; left: 40px; top: 660px; }
  .headline .big { font-weight: 900; font-size: 76px; color: var(--orange); line-height: 1; letter-spacing: 1px; }
  .headline .sub { font-weight: 900; font-size: 38px; color: var(--ink); line-height: 1.2; }
  .services-tag { position: absolute; left: 40px; top: 780px; background: var(--orange); color: #fff; font-weight: 700;
    font-size: 20px; padding: 6px 40px 6px 16px; clip-path: polygon(0 0, 100% 0, 92% 100%, 0 100%); }
  .services { position: absolute; top: 830px; list-style: none; }
  .services.left { left: 40px; }
  .services.right { left: 310px; width: 220px; }
  .services li { display: flex; align-items: center; gap: 12px; font-weight: 600; font-size: 19px; height: 36px; color: #333; }
  .services.right li { height: 56px; line-height: 1.15; }
  .services .icon { width: 28px; height: 28px; border-radius: 50%; background: var(--grey-light); flex: none; }
  .warranty { position: absolute; left: 40px; top: 1015px; width: 500px; height: 70px; background: var(--grey);
    border: 2px dashed #cfd0d2; outline: 4px solid var(--grey); color: #fff; font-weight: 700; font-size: 20px;
    display: flex; flex-direction: column; justify-content: center; align-items: center; line-height: 1.3; }
  .warranty em { font-style: normal; color: var(--orange-light); }
  .certs { position: absolute; left: 40px; top: 1100px; display: flex; align-items: center; gap: 10px; font-size: 13px; font-weight: 600; color: #333; }
  .certs .badge { width: 46px; height: 22px; background: #c7322a; }
  .certs .partner { font-weight: 700; color: var(--orange); }
  .certs .partner.red { color: #d0202a; }
  .follow { position: absolute; left: 370px; top: 1100px; font-size: 13px; font-weight: 600; color: #333; display: flex; align-items: center; gap: 6px; }
  .follow .dot { width: 12px; height: 12px; border-radius: 50%; background: #c7322a; }
  .follow .dot.blue { background: #2c4f9e; border-radius: 2px; }
  .call-band { position: absolute; left: 0; bottom: 0; width: 640px; height: 64px; background: var(--orange);
    clip-path: polygon(0 0, 100% 0, 93% 100%, 0 100%); color: #fff; font-weight: 800; font-size: 28px;
    display: flex; align-items: center; gap: 24px; padding-left: 40px; }
  .call-band svg { width: 30px; height: 30px; }
  .web-band { position: absolute; right: 0; bottom: 0; width: 260px; height: 150px; background: var(--charcoal);
    clip-path: polygon(30% 0, 100% 0, 100% 100%, 0 100%); color: #fff; font-size: 16px; font-weight: 500;
    display: flex; align-items: center; justify-content: flex-end; gap: 10px; padding-right: 22px; }
  .web-band .globe { width: 16px; height: 16px; border-radius: 50%; background: var(--orange); }
</style>
</head>
<body>
<main class="flyer">
  <div class="hero-photo" role="img" aria-label="Roofer in hard hat and safety vest working on an asphalt shingle roof"></div>
  <div class="logo-slab"><span class="mark"></span><span class="name">NO K.W</span></div>

  <div class="gallery">
    <div class="photo roof" role="img" aria-label="Crew working on a shingle roof against blue sky"></div>
    <div class="photo siding" role="img" aria-label="Gloved hands installing new siding"></div>
    <div class="photo gutter" role="img" aria-label="White gutter and downspout under roof eaves"></div>
  </div>

  <div class="headline">
    <div class="big">RELIABILITY</div>
    <div class="sub">STARTS AT THE TOP</div>
  </div>
  <div class="services-tag">OUR SERVICES</div>

  <ul class="services left">
    <li><span class="icon"></span>Roof Installation</li>
    <li><span class="icon"></span>Roof Repair</li>
    <li><span class="icon"></span>Attic ventilation</li>
    <li><span class="icon"></span>Siding Repair</li>
    <li><span class="icon"></span>Gutters</li>
  </ul>
  <ul class="services right">
    <li><span class="icon"></span><span>Commercial<br>Roofing</span></li>
    <li><span class="icon"></span><span>New Siding<br>Installation</span></li>
    <li><span class="icon"></span><span>Roof<br>Inspection</span></li>
  </ul>

  <div class="warranty">
    <span>we offer a <em>15 YEAR</em> warranty with</span>
    <span>our platinum roof program</span>
  </div>

  <div class="certs">
    <span>Certified by</span>
    <span class="badge"></span>
    <span class="partner">dwellmatch</span>
    <span class="partner red">QUARNO</span>
  </div>
  <div class="follow">
    <span>Follow us:</span>
    <span class="dot"></span><span class="dot"></span><span class="dot blue"></span>
    <span>ktwroofing</span>
  </div>

  <div class="web-band"><span class="globe"></span>www.ktw-roofing.com</div>
  <div class="call-band">
    <span>Call us today!</span>
    <svg viewBox="0 0 24 24" aria-hidden="true"><path fill="#1e1f22" d="M6.6 10.8a15.1 15.1 0 0 0 6.6 6.6l2.2-2.2a1 1 0 0 1 1-.25 11.4 11.4 0 0 0 3.6.57 1 1 0 0 1 1 1V20a1 1 0 0 1-1 1A17 17 0 0 1 3 4a1 1 0 0 1 1-1h3.5a1 1 0 0 1 1 1c0 1.25.2 2.45.57 3.57a1 1 0 0 1-.25 1z"/></svg>
    <span>716-555-0147</span>
  </div>
</main>
</body>
</html>
```